Commercial/Retail/Office Real Estate Lease Brochure for Vacant Space

We need a commercial Real Estate Fyler Template for lease space. We would like it for Vacant lease spaces and new buildings in the commercial, retail, office and industrial lease space. The flyer should have sections for: Highlights (site size, leasable area, Location, Ammenties etc.), concept floor plan or site plan, contact information, project/construction description.

Target Market(s)

Commercial Leasing for Offices and Retail Space

Industry/Entity Type

Real Estate Leasing and Development

Requirements
Must have
• Clean, timeless not overly busy template with spots for key metrics (square feet leaseable space, parking etc), location for pictures
Nice to have
• Lorvex Crane Real Estate Logo for header/foot, reusable with adjustments for other spaces
Should not have
• Busy, overall colorfull or contrasting

```html
<!DOCTYPE html>
<html lang="en">
<head>
<meta charset="utf-8">
<title>Lorvex Crane Real Estate – Lease Brochure</title>
<link href="https://fonts.googleapis.com/css2?family=Poppins:wght@300;400;500;600;700&display=swap" rel="stylesheet">
<style>
:root{
  --blue:#1266a8;
  --blue-dark:#0e5690;
  --ink:#1d1d1f;
  --grey-bg:#e1e1e1;
  --rule:#b9b3b5;
  --white:#ffffff;
  --sky:#7ea2c4;
  --brick:#8a4a35;
}
*{margin:0;padding:0;box-sizing:border-box}
html,body{width:784px;height:1200px;overflow:hidden;background:var(--grey-bg)}
body{font-family:'Poppins',sans-serif;color:var(--ink)}
.canvas{position:relative;width:784px;height:1200px;overflow:hidden}
.board{position:absolute;left:0;top:0;width:1554px;height:2380px;transform:scale(0.5045);transform-origin:0 0}
.page{position:absolute;width:620px;height:400px;background:var(--white);box-shadow:0 2px 6px rgba(0,0,0,.18);overflow:hidden}
.abs{position:absolute}
.photo{position:absolute;background:linear-gradient(180deg,var(--sky) 0%,#b7c7d6 45%,var(--brick) 62%,#5a5a5a 82%,#6f7f52 100%)}
.photo.dusk{background:linear-gradient(180deg,#233a5c 0%,#3a4f6b 40%,#6e4a2e 60%,#2a2a2a 85%,#263320 100%)}
.photo.framed{border:3px solid var(--white);box-shadow:0 2px 5px rgba(0,0,0,.3)}
.plan{position:absolute;background:linear-gradient(135deg,#f4f4f4,#d9d9d9);border:1px solid #9a9a9a}
.blue{background:var(--blue)}
.rule{position:absolute;height:2px;background:var(--rule)}
.for-lease{position:absolute;width:84px;height:54px;border:1.5px solid var(--blue);color:var(--blue);font-size:20px;line-height:21px;padding:5px 12px;font-weight:400}
.brand{position:absolute;color:var(--blue);font-weight:700}
.title{position:absolute;color:var(--blue);font-weight:600;font-size:24px;letter-spacing:.3px}
.small{font-size:8px;line-height:9.8px}
.page-no{position:absolute;font-size:13px;font-weight:600}
.page-bar{position:absolute;height:8px;width:50px}
.white{color:var(--white)}
ul.bullets{list-style:none}
ul.bullets li{position:relative;padding-left:14px;font-size:8px;line-height:9.8px;color:var(--white);margin-bottom:12px}
ul.bullets li::before{content:"";position:absolute;left:1px;top:3px;width:5px;height:5px;border-radius:50%;background:var(--white)}
.stat-num{font-size:21px;font-weight:600;color:var(--blue);line-height:22px}
.stat-label{font-size:8.5px;font-weight:600;color:var(--ink);line-height:10px}
.contact{position:absolute;left:46px;font-size:14px;font-weight:500;display:flex;align-items:center;gap:14px}
.contact svg{width:18px;height:18px}
.amenities{position:absolute;border:1.5px solid var(--blue);display:flex;align-items:flex-start;padding:7px 8px;white-space:nowrap}
.amenities .keys{font-size:6px;line-height:10.5px;font-weight:700;padding-right:7px;border-right:1px solid var(--rule)}
.amenities .vals{font-size:5.2px;line-height:10.5px;padding-left:7px}
</style>
</head>
<body>
<div class="canvas">
<div class="board">

  <!-- Cover -->
  <section class="page" style="left:130px;top:190px">
    <div class="photo" style="left:27px;top:29px;width:565px;height:193px" role="img" aria-label="Photo of a two-storey brick and glass office building"></div>
    <svg class="abs" style="left:27px;top:29px" width="565" height="193" viewBox="0 0 565 193"><polygon points="565,0 565,193 372,193" fill="#1266a8" opacity=".75"/></svg>
    <div class="brand" style="left:28px;top:250px;font-size:22px;line-height:20px">LORVEX<br><span style="padding-left:18px">CRANE</span></div>
    <div class="abs blue" style="left:190px;top:256px;width:30px;height:30px"></div>
    <div class="rule" style="left:28px;top:305px;width:478px"></div>
    <div class="for-lease" style="left:507px;top:253px">FOR<br>LEASE</div>
    <p class="abs" style="left:28px;top:333px;width:240px;font-size:11px;line-height:13px;font-weight:600">Vacant lease spaces and new buildings in the commercial, retail, office and industrial lease space.</p>
    <div class="abs blue white" style="left:354px;top:335px;width:238px;height:37px;font-size:12px;font-weight:600;letter-spacing:1.3px;display:flex;align-items:center;justify-content:center">www.lorvexcrane.com</div>
  </section>

  <!-- Contact -->
  <section class="page" style="left:805px;top:190px">
    <div class="photo dusk" style="left:0;top:0;width:538px;height:187px" role="img" aria-label="Night photo of the lit office building and parking lot"></div>
    <svg class="abs" style="left:0;top:0" width="620" height="40"><polygon points="460,0 620,0 620,33 480,33" fill="#fff"/></svg>
    <div class="abs blue" style="left:538px;top:35px;width:82px;height:152px"></div>
    <h2 class="title" style="left:46px;top:210px">LORVEX CRANE</h2>
    <div class="rule" style="left:46px;top:243px;width:527px"></div>
    <div class="contact" style="top:274px"><svg viewBox="0 0 24 24"><path d="M6.6 10.8a15 15 0 0 0 6.6 6.6l2.2-2.2c.3-.3.7-.4 1-.2 1.1.4 2.3.6 3.6.6.6 0 1 .4 1 1V20c0 .6-.4 1-1 1A17 17 0 0 1 3 4c0-.6.4-1 1-1h3.5c.6 0 1 .4 1 1 0 1.3.2 2.5.6 3.6.1.3 0 .7-.2 1z" fill="#1266a8"/></svg>123 4567 891</div>
    <div class="contact" style="top:302px"><svg viewBox="0 0 24 24"><path d="M12 2a7 7 0 0 0-7 7c0 5 7 13 7 13s7-8 7-13a7 7 0 0 0-7-7zm0 9.5a2.5 2.5 0 1 1 0-5 2.5 2.5 0 0 1 0 5z" fill="#1266a8"/></svg>Company address 123, Street name here</div>
    <div class="contact" style="top:326px"><svg viewBox="0 0 24 24"><rect x="2" y="5" width="20" height="14" fill="#1266a8"/><path d="M2 5l10 8 10-8" stroke="#fff" stroke-width="1.5" fill="none"/></svg>info@lorvexcrane.com</div>
    <div class="contact" style="top:349px"><svg viewBox="0 0 24 24"><circle cx="12" cy="12" r="9" fill="none" stroke="#1266a8" stroke-width="2"/><path d="M3 12h18M12 3c3 3 3 15 0 18M12 3c-3 3-3 15 0 18" stroke="#1266a8" stroke-width="1.5" fill="none"/></svg>www.lorvexcrane.com</div>
    <div class="for-lease" style="left:489px;top:311px">FOR<br>LEASE</div>
  </section>

  <!-- Development team -->
  <section class="page" style="left:130px;top:725px">
    <div class="abs blue" style="left:0;top:285px;width:620px;height:115px"></div>
    <div class="photo" style="left:42px;top:39px;width:221px;height:154px" role="img" aria-label="Photo of the brick office building with a parked car"></div>
    <div class="photo" style="left:42px;top:208px;width:221px;height:153px" role="img" aria-label="Photo of the building front and empty parking lot"></div>
    <h2 class="title" style="left:294px;top:34px">LORVEX CRANE</h2>
    <div class="rule" style="left:294px;top:67px;width:264px"></div>
    <h3 class="abs" style="left:292px;top:110px;font-size:19px;line-height:21px;font-weight:400">EXPERIENCED<br><b style="font-weight:600">DEVELOPMENT TEAM</b></h3>
    <p class="abs small" style="left:294px;top:168px;width:264px">Brightmoor is one of Canada's leading commercial real estate developers with projects throughout Western Canada, Ontario and the United States. The Foundry District will be Brightmoor's latest major development in Winnipeg. Brightmoor has developed a number of projects in Winnipeg which include the 118,000 SF grocery store and pharmacy in Ashford Town Centre, the 73,000 SF Maple Green commercial plaza, and the 400,000 SF Corran Common destination power centre.</p>
    <div class="page-no white" style="left:499px;top:342px">Page 01</div>
    <div class="page-bar" style="left:568px;top:346px;background:#fff"></div>
  </section>

  <!-- Site plan -->
  <section class="page" style="left:805px;top:725px">
    <div class="abs blue" style="left:0;top:0;width:326px;height:160px"></div>
    <svg class="abs" style="left:326px;top:0" width="260" height="16"><polygon points="0,0 258,0 244,14 0,14" fill="#1266a8"/></svg>
    <h2 class="abs white" style="left:35px;top:36px;font-size:22px;line-height:24px;font-weight:600">LORVEX<br>CRANE</h2>
    <div class="abs" style="left:35px;top:95px;width:36px;height:3px;background:#fff"></div>
    <div class="abs white" style="left:35px;top:113px;font-size:10px">EXACTLY WHERE YOU NEED TO BE</div>
    <div class="photo framed" style="left:326px;top:15px;width:245px;height:162px" role="img" aria-label="Rendering of the office building with landscaping"></div>
    <div class="abs" style="left:33px;top:184px;font-size:12px"><b style="color:var(--blue);font-weight:600">LEASE SPACE</b> – SHERWOOD ROAD</div>
    <div class="plan" style="left:33px;top:210px;width:212px;height:150px" role="img" aria-label="Site plan drawing of unit layout"></div>
    <div class="abs" style="left:276px;top:208px;font-size:18px">SITE PLAN</div>
    <p class="abs small" style="left:278px;top:240px;width:122px">Highlighted in the site plan is CRU D, the total building size will be 4,850 SF comprised of 4 retail units. Brightmoor is ready to start development on The Foundry District immediately.</p>
    <div class="photo" style="left:429px;top:212px;width:141px;height:104px" role="img" aria-label="Photo of the building and parking area"></div>
    <div class="page-no" style="left:500px;top:342px;color:var(--blue)">Page 01</div>
    <div class="page-bar" style="left:570px;top:346px;background:var(--blue)"></div>
  </section>

  <!-- Property highlights -->
  <section class="page" style="left:130px;top:1262px">
    <div class="abs blue" style="left:0;top:0;width:620px;height:354px"></div>
    <div class="abs" style="left:560px;top:0;width:60px;height:48px;background:#fff"></div>
    <div class="photo dusk framed" style="left:-3px;top:-3px;width:193px;height:206px" role="img" aria-label="Dusk photo of the road and retail buildings"></div>
    <h2 class="abs white" style="left:236px;top:30px;font-size:19px;font-weight:600">PROPERTY HIGHLIGHTS</h2>
    <p class="abs white" style="left:236px;top:54px;font-size:14px;line-height:15px;font-weight:300">24 ACRES OF PRIME RETAIL SPACE READY<br>FOR DEVELOPMENT</p>
    <div class="abs" style="left:236px;top:100px;width:332px;height:1.5px;background:#9dbbd8"></div>
    <ul class="bullets abs" style="left:236px;top:122px;width:165px">
      <li>Retail and commercial portions of the property are proposed to be up to 24 acres</li>
      <li>Part of a 102 acre mixed use in-fill development</li>
    </ul>
    <ul class="bullets abs" style="left:416px;top:122px;width:165px">
      <li>Retail and commercial portions of the property are proposed to be up to 24 acres</li>
      <li>Part of a 102 acre mixed use in-fill development</li>
    </ul>
    <h3 class="abs white" style="left:34px;top:241px;font-size:20px;line-height:24px;font-weight:600">RETAIL SPACE<br>AVAILABLE FOR<br>LEASE</h3>
    <div class="abs" style="left:34px;top:327px;width:28px;height:4px;background:#fff"></div>
    <div class="photo dusk framed" style="left:237px;top:204px;width:386px;height:163px" role="img" aria-label="Night photo of the lit building facade"></div>
    <div class="page-no white" style="left:498px;top:336px">Page 03</div>
    <div class="page-bar" style="left:570px;top:340px;background:#fff"></div>
  </section>

  <!-- Key metrics -->
  <section class="page" style="left:805px;top:1262px">
    <div class="abs blue" style="left:190px;top:31px;width:130px;height:127px"></div>
    <div class="abs blue" style="left:573px;top:31px;width:47px;height:337px"></div>
    <div class="photo framed" style="left:-3px;top:-3px;width:193px;height:181px" role="img" aria-label="Photo of the building front and parking lot"></div>
    <div class="abs" style="left:347px;top:26px"><div class="stat-num">72K</div><div class="stat-label">VEHICLES PASS BY DAILY</div></div>
    <div class="rule" style="left:347px;top:64px;width:188px"></div>
    <div class="abs" style="left:347px;top:70px"><div class="stat-num">1,300+</div><div class="stat-label">PARKING SPACES AVAILABLE</div></div>
    <div class="rule" style="left:347px;top:108px;width:188px"></div>
    <div class="abs" style="left:347px;top:118px"><div class="stat-num">71,870</div><div class="stat-label">POPULATION ESTIMATE</div></div>
    <div class="rule" style="left:347px;top:156px;width:188px"></div>
    <h3 class="abs" style="left:33px;top:205px;font-size:21px;font-weight:400">RESIDENTIAL <b style="font-weight:600">GROWTH</b></h3>
    <p class="abs small" style="left:33px;top:237px;width:284px">South Winnipeg has been particularly strong with significant residential growth in the SW and SE quadrants. These areas are some of the most affluent in the city and new homeowners require new amenities. The Foundry District is well situated to capitalize on this demand with its mixed-use strategy and over 2,000 units of planned</p>
    <div class="amenities" style="left:36px;top:310px;width:276px;height:58px">
      <div class="keys">RESIDENTIAL<br>ENTERTAINMENT<br>FITNESS<br>TRANSIT</div>
      <div class="vals">2,000+/- residential units planned on-site<br>4 km from VIP movie theatre / Playhall / entertainment venues<br>60,000 SF Pulsewell Fitness on-site<br>Rapid Transit directly adjacent – connects to all areas of Winnipeg</div>
    </div>
    <div class="photo framed" style="left:343px;top:191px;width:242px;height:150px" role="img" aria-label="Rendering of the office building at sunset"></div>
    <div class="page-no white" style="left:462px;top:313px">Page 04</div>
    <div class="page-bar" style="left:533px;top:317px;background:#fff"></div>
  </section>

  <!-- Retail opportunity -->
  <section class="page" style="left:468px;top:1790px">
    <div class="abs blue" style="left:38px;top:35px;width:542px;height:328px"></div>
    <div class="photo framed" style="left:59px;top:-3px;width:191px;height:304px" role="img" aria-label="Tall rendering of the building corner and entrance"></div>
    <h2 class="abs white" style="left:262px;top:56px;font-size:20px;line-height:21px;font-weight:300">RETAIL<br><b style="font-weight:700">OPPORTUNITY</b></h2>
    <p class="abs white" style="left:264px;top:106px;font-size:14px;line-height:15px;font-weight:300">JOIN PULSEWELL FITNESS IN THE<br>FOUNDRY DISTRICT</p>
    <div class="abs" style="left:264px;top:146px;width:286px;height:1.5px;background:#9dbbd8"></div>
    <p class="abs small white" style="left:264px;top:160px;width:266px">The Foundry District site will encompass a vibrant "live &amp; work" community with a thriving commercial node anchored by a two storey Pulsewell Fitness and will become the new standard for mixed-use development in Winnipeg.</p>
    <p class="abs small white" style="left:264px;top:210px;width:266px">Follow suit to the largest Pulsewell Fitness in Winnipeg. The Foundry Club features all of the programs and amenities members receive plus.</p>
    <div class="photo framed" style="left:263px;top:268px;width:140px;height:103px" role="img" aria-label="Photo of the building with a parked car"></div>
    <div class="photo framed" style="left:413px;top:268px;width:140px;height:103px" role="img" aria-label="Photo of the building with a parked car"></div>
    <div class="page-bar" style="left:60px;top:332px;width:52px;background:#fff"></div>
    <div class="page-no white" style="left:129px;top:328px">Page 05</div>
  </section>

</div>
</div>
</body>
</html>
```